GRHWC 2026 Theme for Wall Banners

We need a design created for a wall banner 4 x 4 feet, for our church's 2026 Theme:
"Applying God's Word"
"Acquiring God's Wisdom"
"Acknowledging God's Will"
"Advancing God's Work"
Proverbs 3:5-6

Use the church's colors purple, silver, white and include the logo
Church Name: Grace-Rooted Harvest Church of Willow Creek

Target Market(s)

Male & Female, ages 0-99

Industry/Entity Type

Religious, church

Colors
6B429C
8869AF
B7A5CE
E3DAEB
F3F0F8

Requirements
Must have
• Logo, colors, use of all 4 phrases; use of scripture text
Nice to have
• Maybe the phrases in / on pillars
Should not have
• Images or language that is non-Christian

```html
<!DOCTYPE html>
<html lang="en">
<head>
<meta charset="utf-8">
<title>GRHWC 2026 Theme Banner</title>
<link rel="stylesheet" href="https://fonts.googleapis.com/css2?family=Oswald:wght@500;600&family=Playfair+Display:ital,wght@1,700&family=Poppins:wght@700&display=swap">
<style>
  :root {
    --purple: #6B429C;
    --purple-mid: #8869AF;
    --lavender: #B7A5CE;
    --lilac: #E3DAEB;
    --mist: #F3F0F8;
    --white: #FFFFFF;
    --ink: #111111;
    --silver: #C9C9CF;
  }
  html, body {
    margin: 0;
    width: 1200px;
    height: 613px;
    overflow: hidden;
    background: var(--white);
  }
  .banner {
    position: absolute;
    top: 20px;
    width: 573px;
    height: 573px;
    overflow: hidden;
  }
  .banner--purple { left: 21px; background: var(--purple); --text: var(--white); --wreath: var(--white); }
  .banner--light { left: 606px; background: var(--mist); --text: var(--ink); --wreath: var(--purple); }

  .wreath { position: absolute; inset: 0; }
  .wreath path { fill: none; stroke: var(--wreath); stroke-linecap: round; }
  .banner--purple .wreath path { stroke-width: 34; }
  .banner--light .wreath path { stroke-width: 30; }

  .church-mark {
    position: absolute;
    left: 0; right: 0;
    top: 46px;
    display: flex;
    flex-direction: column;
    align-items: center;
    gap: 8px;
  }
  .banner--light .church-mark { top: 52px; }
  .church-mark__disc {
    width: 92px; height: 92px;
    border-radius: 50%;
    background: var(--silver);
  }
  .church-mark__name {
    font-family: "Oswald", sans-serif;
    font-weight: 600;
    font-size: 20px;
    letter-spacing: 2px;
    color: var(--text);
    line-height: 1;
  }

  .theme {
    position: absolute;
    left: 0; right: 0;
    top: 200px;
    margin: 0;
    padding: 0;
    list-style: none;
    text-align: center;
    color: var(--text);
  }
  .banner--light .theme { top: 202px; }
  .theme__line {
    height: 48px;
    line-height: 48px;
    white-space: nowrap;
    transform: scaleX(0.8);
    transform-origin: center;
  }
  .theme__verb {
    font-family: "Oswald", sans-serif;
    font-weight: 600;
    font-size: 38px;
    letter-spacing: -0.5px;
  }
  .theme__object {
    font-family: "Playfair Display", serif;
    font-style: italic;
    font-weight: 700;
    font-size: 30px;
    letter-spacing: -0.8px;
    margin-left: 8px;
  }

  .scripture {
    position: absolute;
    left: 0; right: 0;
    top: 424px;
    margin: 0;
    text-align: center;
    font-family: "Poppins", sans-serif;
    font-weight: 700;
    font-size: 11px;
    letter-spacing: 0.3px;
    color: var(--text);
  }
  .banner--light .scripture { top: 413px; }

  .cross {
    position: absolute;
    left: 275px;
    top: 483px;
    width: 30px; height: 37px;
  }
  .banner--light .cross { left: 272px; top: 466px; }
  .cross rect { fill: var(--text); }

  .footer-name {
    position: absolute;
    left: 0; right: 0;
    top: 526px;
    margin: 0;
    padding-left: 6px;
    text-align: center;
    font-family: "Oswald", sans-serif;
    font-weight: 500;
    font-size: 8.5px;
    line-height: 11px;
    color: var(--text);
  }
  .banner--light .footer-name { top: 510px; padding-left: 0; }
</style>
</head>
<body>

<section class="banner banner--purple">
  <svg class="wreath" viewBox="0 0 573 573" role="img" aria-label="Laurel wreath framing the theme">
    <path d="M140 100 C 15 230, 40 450, 235 492"/>
    <path d="M433 100 C 558 230, 533 450, 338 492"/>
  </svg>
  <div class="church-mark">
    <div class="church-mark__disc"></div>
    <div class="church-mark__name">GRHWC</div>
  </div>
  <ul class="theme">
    <li class="theme__line"><span class="theme__verb">APPLYING</span><span class="theme__object">God's Word</span></li>
    <li class="theme__line"><span class="theme__verb">ACKNOWLEDGING</span><span class="theme__object">God's Will</span></li>
    <li class="theme__line"><span class="theme__verb">ADVANCING</span><span class="theme__object">God's Work</span></li>
    <li class="theme__line"><span class="theme__verb">ACQUIRING</span><span class="theme__object">God's Wisdom</span></li>
  </ul>
  <p class="scripture">PROVERBS 3:5-6</p>
  <svg class="cross" viewBox="0 0 30 37" aria-hidden="true">
    <rect x="12" y="0" width="6" height="37"/>
    <rect x="0" y="9" width="30" height="6"/>
  </svg>
  <p class="footer-name">GRACE-ROOTED HARVEST CHURCH<br>OF WILLOW CREEK</p>
</section>

<section class="banner banner--light">
  <svg class="wreath" viewBox="0 0 573 573" role="img" aria-label="Laurel wreath framing the theme">
    <path d="M150 135 C 55 260, 75 430, 222 478"/>
    <path d="M423 135 C 518 260, 498 430, 351 478"/>
  </svg>
  <div class="church-mark">
    <div class="church-mark__disc"></div>
    <div class="church-mark__name">GRHWC</div>
  </div>
  <ul class="theme">
    <li class="theme__line"><span class="theme__verb">APPLYING</span><span class="theme__object">God's Word</span></li>
    <li class="theme__line"><span class="theme__verb">ACKNOWLEDGING</span><span class="theme__object">God's Will</span></li>
    <li class="theme__line"><span class="theme__verb">ADVANCING</span><span class="theme__object">God's Work</span></li>
    <li class="theme__line"><span class="theme__verb">ACQUIRING</span><span class="theme__object">God's Wisdom</span></li>
  </ul>
  <p class="scripture">PROVERBS 3:5-6</p>
  <svg class="cross" viewBox="0 0 30 37" aria-hidden="true">
    <rect x="12" y="0" width="6" height="37"/>
    <rect x="0" y="9" width="30" height="6"/>
  </svg>
  <p class="footer-name">GRACE-ROOTED HARVEST CHURCH<br>OF WILLOW CREEK</p>
</section>

</body>
</html>
```